Kellwood Build, Carpentry Services

Business card for carpentry business in the Sunshine Coast.

Business card layout required using logo provided - provided both PDF copy and AI. Please let me know if you would like a the files for the logo symbol and text by itself.

Business Colours are grey, blue and white. The font colours codes for this design are Blue Hex # 00B4E6 and Hex # 39393B for the gray colour.

FYI font for logo is Gotham Bold.

Preference for a clean and striking layout that is simple and elegant.

Target Market(s)

Young Families, retirees, young couples requiring assistance with small to medium works/renovations on the Sunshine Coast.

Industry/Entity Type

Construction

Contact Information for Business Card

Dean Kellwood
Carpenter
0489305627
dean@kellwoodbuild.com.au
Kestrel Point, Palm Coast
RHPA Licensed Carpenter (In smaller font)

Font styles to use
Sans Serif

Colors

Designer to choose colors to be used in the design.

Requirements
Must have
• Logo provided must appear on the card, preferably on one side of the card by itself with the text on the alternate side
Nice to have
• Text on the other side of card, maybe grey background and white font here but happy for the designer to provide ideas here.
Should not have
• Use of other colours, other than the ones provided - white, grey and blue. Black optional.

```html
<!DOCTYPE html>
<html lang="en">
<head>
<meta charset="utf-8">
<title>Kellwood Build – Business Card</title>
<link rel="stylesheet" href="https://fonts.googleapis.com/css2?family=Montserrat:wght@500;700&family=Arimo:wght@400;700&display=swap">
<style>
  :root {
    --backdrop: #3b3836;
    --card: #0e0e0f;
    --card-edge: #1c1c1e;
    --blue: #00b4e6;
    --grey: #39393b;
    --white: #ffffff;
    --soft-white: #d8d8d8;
  }
  * { box-sizing: border-box; margin: 0; padding: 0; }
  html, body {
    width: 1200px; height: 844px; overflow: hidden;
    background: var(--backdrop);
  }
  .canvas {
    position: relative; width: 1200px; height: 844px;
    display: flex; align-items: center; justify-content: center; gap: 40px;
  }
  .card {
    position: relative; width: 540px; height: 309px;
    background: var(--card);
    border: 1px solid var(--card-edge);
    border-radius: 3px;
    box-shadow: 0 14px 30px rgba(0,0,0,.45);
    overflow: hidden;
  }

  /* Contact side */
  .card--contact { display: flex; }
  .brand-panel {
    width: 216px; height: 100%;
    display: flex; align-items: center; justify-content: center; gap: 10px;
    border-right: 1px solid var(--grey);
  }
  .brand-mark { width: 14px; height: 14px; background: var(--blue); flex: none; }
  .brand-name {
    font-family: "Montserrat", sans-serif; font-weight: 700;
    font-size: 21px; letter-spacing: .5px; color: var(--blue);
    line-height: 1.15; text-transform: uppercase;
  }
  .contact-panel {
    flex: 1; padding: 70px 0 0 34px;
    font-family: "Arimo", sans-serif; color: var(--soft-white);
  }
  .person-name {
    font-family: "Arimo", sans-serif; font-weight: 700;
    font-size: 19px; color: var(--blue); text-transform: uppercase;
    letter-spacing: .3px;
  }
  .person-role { font-size: 14px; color: var(--white); margin: 2px 0 18px; }
  .contact-list { list-style: none; }
  .contact-item {
    display: flex; align-items: center; gap: 9px;
    font-size: 14px; margin-bottom: 9px; color: var(--soft-white);
    white-space: nowrap;
  }
  .contact-item svg { width: 16px; height: 16px; flex: none; }
  .contact-item--location { font-size: 16px; margin-top: 6px; }

  /* Brand side */
  .card--brand {
    display: flex; flex-direction: column; align-items: center; justify-content: center;
  }
  .brand-lockup { display: flex; align-items: center; gap: 14px; }
  .brand-lockup .brand-mark { width: 18px; height: 18px; background: var(--soft-white); }
  .brand-title {
    font-family: "Montserrat", sans-serif; font-weight: 700;
    font-size: 32px; letter-spacing: 2px; color: var(--soft-white);
    text-transform: uppercase;
  }
  .licence {
    margin-top: 38px;
    font-family: "Arimo", sans-serif; font-size: 11px;
    color: var(--soft-white); letter-spacing: .3px;
  }
</style>
</head>
<body>
<main class="canvas">

  <section class="card card--contact" aria-label="Business card, contact side">
    <div class="brand-panel">
      <span class="brand-mark"></span>
      <span class="brand-name">Kellwood<br>Build</span>
    </div>
    <div class="contact-panel">
      <h1 class="person-name">Dean Kellwood</h1>
      <p class="person-role">Carpenter</p>
      <ul class="contact-list">
        <li class="contact-item">
          <svg viewBox="0 0 16 16" aria-hidden="true"><rect x="1" y="1" width="14" height="14" rx="2" fill="none" stroke="#00b4e6" stroke-width="1.5"/><path d="M5 4.5c0 4 2.5 6.5 6.5 7l1-1.5-2-1-1 1c-1.3-.6-2.4-1.7-3-3l1-1-1-2z" fill="#00b4e6"/></svg>
          0489305627
        </li>
        <li class="contact-item">
          <svg viewBox="0 0 16 16" aria-hidden="true"><rect x="1" y="3" width="14" height="10" fill="#00b4e6"/><path d="M1 3l7 5.5L15 3" fill="none" stroke="#0e0e0f" stroke-width="1.3"/></svg>
          dean@kellwoodbuild.com.au
        </li>
        <li class="contact-item contact-item--location">
          <svg viewBox="0 0 16 16" aria-hidden="true"><path d="M8 1a5 5 0 0 0-5 5c0 3.8 5 9 5 9s5-5.2 5-9a5 5 0 0 0-5-5z" fill="#00b4e6"/><circle cx="8" cy="6" r="1.8" fill="#0e0e0f"/></svg>
          Kestrel Point, Palm Coast
        </li>
      </ul>
    </div>
  </section>

  <section class="card card--brand" aria-label="Business card, brand side">
    <div class="brand-lockup">
      <span class="brand-mark"></span>
      <span class="brand-title">Kellwood Build</span>
    </div>
    <p class="licence">RHPA Licensed Carpenter</p>
  </section>

</main>
</body>
</html>
```